Startup photography business has a new logo, now we need business cards

Design a business card for the two partners of our business.
Our business Brisk Pelican has a new logo and we need to design a business card to showcase it and us.
Our colours of blue and orange are punchy and vivid, but how can we make the most of it on our card?

It should have our name Brisk Pelican
name of partner
phone number
email
website

Industry/Entity Type

Professional Photography

Contact Information for Business Card

Tom Ashworth
+61 400 55 61 72
tom@briskpelican.com.au
briskpelican.com.au

second card
Neil Porter
+61 400 918 263
tom@briskpelican.com.au
briskpelican.com.au

Colors
f37122
f68d4c
33a6d7
0592cd

Requirements
Must have
• one version of our logo, we have included options
• Name
• phone number
• email
• website
Nice to have
• instagram briskpelicanmedia
• twitter briskpelicanmedia
• facebook briskpelicanmedia

```html
<!DOCTYPE html>
<html lang="en">
<head>
<meta charset="utf-8">
<title>Brisk Pelican – Business Cards</title>
<link href="https://fonts.googleapis.com/css2?family=Open+Sans:wght@400;600;700&display=swap" rel="stylesheet">
<style>
  :root {
    --orange: #f37122;
    --orange-soft: #f68d4c;
    --blue: #33a6d7;
    --blue-deep: #0592cd;
    --ink: #2a2a2a;
    --paper: #ffffff;
    --stage: #e9e6e2;
  }
  * { box-sizing: border-box; margin: 0; padding: 0; }
  html, body {
    width: 1200px; height: 900px; overflow: hidden;
    background: var(--stage);
    font-family: "Open Sans", Arial, sans-serif;
  }
  .stage { position: relative; width: 1200px; height: 900px; }

  .card {
    position: absolute; left: 290px;
    width: 620px; height: 354px;
    box-shadow: 0 10px 28px rgba(0,0,0,.18);
    overflow: hidden;
  }

  /* Back of card */
  .card-back { top: 60px; background: var(--orange); color: var(--paper); }
  .social {
    position: absolute; right: 40px; top: 40px;
    list-style: none; font-size: 17px; line-height: 1.9;
  }
  .social-rule {
    position: absolute; right: 40px; top: 150px; width: 230px; height: 2px;
    background: var(--paper);
  }
  .back-brand {
    position: absolute; left: 44px; top: 210px;
    display: flex; align-items: center; gap: 16px;
  }
  .brand-dot { width: 58px; height: 58px; border-radius: 50%; background: var(--paper); flex: none; }
  .back-brand .brand-name {
    font-weight: 700; font-size: 46px; letter-spacing: 1px;
    text-transform: uppercase; color: var(--paper); line-height: 1;
  }
  .back-rule {
    position: absolute; left: 44px; top: 300px; width: 330px; height: 2px;
    background: var(--paper);
  }

  /* Front of card */
  .card-front { top: 486px; background: var(--paper); color: var(--ink); }
  .front-brand {
    position: absolute; left: 0; right: 0; top: 34px;
    display: flex; justify-content: center; align-items: center; gap: 14px;
  }
  .front-brand .brand-dot { width: 50px; height: 50px; background: var(--orange); }
  .front-brand .brand-name {
    font-weight: 700; font-size: 40px; letter-spacing: 1px;
    text-transform: uppercase; color: var(--blue); line-height: 1;
  }
  .front-rule {
    position: absolute; left: 180px; right: 180px; top: 104px; height: 2px;
    background: var(--orange);
  }
  .address {
    position: absolute; left: 40px; top: 122px;
    font-size: 17px; color: var(--ink);
  }
  .band {
    position: absolute; left: 0; right: 0; top: 158px; height: 22px;
    background: var(--orange);
  }
  .person { position: absolute; left: 40px; top: 200px; }
  .person-name { font-weight: 700; font-size: 22px; color: var(--orange); }
  .person-role { font-size: 18px; color: var(--ink); margin-top: 2px; }

  .contacts {
    position: absolute; left: 372px; top: 214px;
    list-style: none; font-size: 16px; color: var(--ink);
  }
  .contacts li { display: flex; align-items: center; gap: 10px; height: 32px; }
  .contacts svg { width: 16px; height: 16px; flex: none; }
</style>
</head>
<body>
<main class="stage">

  <section class="card card-back" aria-label="Card back">
    <ul class="social">
      <li>instagram briskpelicanmedia</li>
      <li>twitter briskpelicanmedia</li>
      <li>facebook briskpelicanmedia</li>
    </ul>
    <div class="social-rule"></div>
    <div class="back-brand">
      <span class="brand-dot"></span>
      <span class="brand-name">Brisk Pelican</span>
    </div>
    <div class="back-rule"></div>
  </section>

  <section class="card card-front" aria-label="Card front">
    <div class="front-brand">
      <span class="brand-dot"></span>
      <span class="brand-name">Brisk Pelican</span>
    </div>
    <div class="front-rule"></div>
    <p class="address">Unit 4, 18 Harbour Lane, Fremantle</p>
    <div class="band"></div>
    <div class="person">
      <p class="person-name">Tom Ashworth</p>
      <p class="person-role">Manager</p>
    </div>
    <ul class="contacts">
      <li>
        <svg viewBox="0 0 16 16" aria-hidden="true"><path fill="#f37122" d="M4 1.5 6.2 4 5 5.6c.8 2 2.4 3.6 4.4 4.4L11 8.8l2.5 2.2-1.2 2.6C7 13.4 2.6 9 2.4 3.7Z"/></svg>
        61 400 55 61 72
      </li>
      <li>
        <svg viewBox="0 0 16 16" aria-hidden="true"><g fill="none" stroke="#f37122" stroke-width="1.4"><circle cx="8" cy="8" r="6.5"/><ellipse cx="8" cy="8" rx="2.8" ry="6.5"/><path d="M1.5 8h13M2.5 4.8h11M2.5 11.2h11"/></g></svg>
        briskpelican.com.au
      </li>
      <li>
        <svg viewBox="0 0 16 16" aria-hidden="true"><text x="8" y="13" text-anchor="middle" font-family="Open Sans, Arial, sans-serif" font-weight="700" font-size="15" fill="#f37122">@</text></svg>
        tom@briskpelican.com.au
      </li>
    </ul>
  </section>

</main>
</body>
</html>
```